依頼詳細
値段は入れず、『不安を安心に』『疑問を納得へ』『生活保護のご葬儀 自己負担0円』と言った文言を入れていただきたいです。
葬儀の流れの図も入れていただきたいです。
※添付ファイルを参照ください。
記載項目
電話番号のところは◯にしておいてください
サイズ
A4
ページ数
片面
希望イメージ
シンプル 複雑
単色 カラフル
暗い 明るい
日常 高級
遊び心 厳粛
未来的 伝統的
女性的 男性的
希望する色
赤系
納品ファイル
• 高解像度JPG (.jpg)
• イラストレーター形式 (.ai)
• フォトショップ形式 (.psd)
• PNG形式 (.png)
補足説明
■ 選んだ理由

シンプルで中身がわかりやすく気に入りました

■ 提案者全員のお礼・コメント

ありがとうございます!!また機会がありましたらお願い致します

```html
<!DOCTYPE html>
<html lang="ja">
<head>
<meta charset="utf-8">
<title>生活保護葬儀の流れ</title>
<link href="https://fonts.googleapis.com/css2?family=Noto+Serif+JP:wght@400;600;700&family=Noto+Sans+JP:wght@400;500;700&display=swap" rel="stylesheet">
<style>
:root{
  --bg-top:#f7c9cf;
  --bg-mid:#fbe3e3;
  --bg-bottom:#f3b4bd;
  --rose:#d98a98;
  --rose-deep:#c46a7c;
  --accent:#d0324a;
  --ink:#3a2a2e;
  --panel:#ffffff;
  --note-bg:#fbeef0;
}
*{margin:0;padding:0;box-sizing:border-box}
html,body{width:849px;height:1200px;overflow:hidden}
body{
  font-family:"Noto Sans JP",sans-serif;
  color:var(--ink);
  background:linear-gradient(160deg,var(--bg-top) 0%,var(--bg-mid) 45%,var(--bg-bottom) 100%);
  position:relative;
}
.brand{
  position:absolute;top:18px;right:36px;
  display:flex;flex-direction:column;align-items:center;
  color:var(--rose-deep);font-family:"Noto Serif JP",serif;font-weight:600;
}
.brand-type{font-size:13px;letter-spacing:2px}
.brand-row{display:flex;align-items:center;gap:8px;margin-top:4px}
.brand-dot{width:22px;height:22px;border-radius:50%;background:var(--rose-deep)}
.brand-name{font-size:30px;letter-spacing:1px}
.tagline{
  position:absolute;top:136px;left:0;width:100%;text-align:center;
  color:var(--accent);font-family:"Noto Serif JP",serif;font-weight:600;font-size:18px;letter-spacing:1px;
}
.title{
  position:absolute;top:166px;left:0;width:100%;text-align:center;
  font-family:"Noto Serif JP",serif;font-weight:700;font-size:46px;letter-spacing:4px;color:#2e2226;
}
.flow{
  position:absolute;left:57px;top:248px;width:735px;height:926px;
  background:var(--panel);padding:14px 18px;
  display:flex;flex-direction:column;justify-content:space-between;
}
.step-head{
  background:linear-gradient(90deg,var(--rose),#e7a6b1,var(--rose));
  color:#fff;text-align:center;font-family:"Noto Serif JP",serif;font-weight:700;
  font-size:19px;letter-spacing:3px;height:32px;line-height:32px;
  clip-path:polygon(0 0,100% 0,100% 100%,52% 100%,50% 112%,48% 100%,0 100%);
}
.step-body{font-size:12px;line-height:1.7;text-align:center;padding:7px 8px 0}
.step-body.left{text-align:left;padding-left:60px}
.phone{
  display:inline-block;margin-top:5px;padding:3px 14px;border:1px solid var(--rose);
  font-weight:700;font-size:13px;background:var(--note-bg)
}
</style>
</head>
<body>
<div class="brand">
  <span class="brand-type">一般社団法人</span>
  <div class="brand-row"><span class="brand-dot"></span><span class="brand-name">Lumiel</span></div>
</div>
<p class="tagline">不安を安心に　生活保護のご葬儀 自己負担0円</p>
<h1 class="title">生活保護葬儀の流れ</h1>

<main class="flow">
  <section class="step">
    <h2 class="step-head">①ご臨終</h2>
    <p class="step-body">生活保護受給者が亡くなられた場合、弊社にご連絡ください。24時間体制でご対応致します。<br>
    <span class="phone">お問い合せ先電話番号：○○○○○○○○○○○○○○○</span></p>
  </section>
  <section class="step">
    <h2 class="step-head">②お迎え</h2>
    <p class="step-body">お亡くなりになられた場所へ弊社寝台車で、専用霊安室までお迎えにあがります。</p>
  </section>
  <section class="step">
    <h2 class="step-head">③ご搬送・ご遺体安置</h2>
    <p class="step-body">ご希望の場所にご搬送・ご安置致します。弊社の遺体保冷室でのご安置も可能です。</p>
  </section>
  <section class="step">
    <h2 class="step-head">④お打合せ</h2>
    <p class="step-body left">① お打合せ・火葬場予約を致します。<br>
    ② 地域の福祉担当者にご遺族様から生活保護葬を行いたい旨のご了解をとりつけて頂き<br>
    　葬儀社の名前を伝えて頂きます。（必要な書類は弊社にてご用意致します）<br>
    ③ 死亡届出書の代理提出（弊社にて行い、火葬許可証を受け取ります）</p>
  </section>
  <section class="step">
    <h2 class="step-head">⑤ご出棺・火葬</h2>
    <p class="step-body">火葬日当日・副葬品・お花などを棺に納めて頂き、ご納棺・ご焼香（お別れ）されたあと、出棺します。<br>
    車で火葬場まで向かわれる場合はお申し出ください。弊社車両でのご案内も可能です。</p>
  </section>
  <section class="step">
    <h2 class="step-head">⑥荼毘</h2>
    <p class="step-body">お別れの会のち火葬がございます。荼毘式までお待ち頂きます。<br>（火葬時間は１時間～１時間３０分）</p>
  </section>
  <section class="step">
    <h2 class="step-head">⑦ご収骨</h2>
    <p class="step-body">ご収骨室にてご収骨致します。骨壺・メモリアル品等を骨壺に納めます。<br>
    ご収骨後、ご遺骨はお持ち帰り頂けます。納骨先のご相談も承ります。</p>
  </section>
  <section class="step">
    <h2 class="step-head">⑧生活保護葬費のご請求申請</h2>
    <p class="step-body">福祉担当者に、生活保護葬の請求申請を致します。福祉事務所・社会保護課への請求は弊社にて行います。</p>
  </section>
</main>
</body>
</html>
```